Business Cards Design for the electrical wholesaler: clean bold dynamic :)

We need a business card design that would follow our latest brand guidelines. As an electrical wholesaler we want to bring a fresh look and feel into the industry. The design should be clean bold and dynamic. It should come alive with the renewed energy of our green colour. Our grey colour should keep things balanced and complement the notion of maturity and responsibility. We employ Lato as a corporate font however are not bound by this font and we’re open to interpretation here.

Target Market(s)

Electrical contractors

Industry/Entity Type

Business

Contact Information for Business Card

Logo
Name & Surname: Olena Dovbush
Job Title: Director of Marketing
Email: helen.dovbush@mailvane.example
Cell phone: XXX.XXX.XXXX
Address: 20917 - 87 Ave. Edmonton, AB, Canada. T6K 2R8
Business Phone: 780.555.0187
Website: www.qorvil.example

Font styles to use
Other font styles liked:
• Lato

Requirements
Must have
• Logo & website
Nice to have
• Brand elements - some of them you may find in the attached Brand Guidelines (e.g. three lines on the background signifying "W")

```html
<!DOCTYPE html>
<html lang="en">
<head>
<meta charset="utf-8">
<title>Qorvil Business Card</title>
<link rel="stylesheet" href="https://fonts.googleapis.com/css2?family=Lato:wght@400;700;900&display=swap">
<style>
  :root {
    --brand-green: #8dc63f;
    --brand-grey: #898989;
    --ink-dark: #545557;
    --paper: #ffffff;
  }
  * { box-sizing: border-box; margin: 0; padding: 0; }
  html, body {
    width: 1200px;
    height: 1000px;
    overflow: hidden;
    background: var(--paper);
    font-family: "Lato", Arial, sans-serif;
  }
  .canvas { position: relative; width: 1200px; height: 1000px; }

  .card-front {
    position: absolute;
    left: 192px; top: 8px;
    width: 816px; height: 489px;
    background: var(--brand-green);
  }
  .front-wordmark {
    position: absolute;
    left: 0; right: 0; top: 120px;
    text-align: center;
    font-weight: 900;
    font-size: 190px;
    line-height: 1;
    letter-spacing: -2px;
    color: var(--ink-dark);
  }
  .front-website {
    position: absolute;
    left: 0; right: 0; top: 414px;
    text-align: center;
    font-size: 15px;
    letter-spacing: 0.3px;
    color: var(--ink-dark);
  }

  .card-back {
    position: absolute;
    left: 192px; top: 501px;
    width: 818px; height: 491px;
    background: var(--brand-grey);
  }
  .back-wordmark {
    position: absolute;
    left: 52px; top: 192px;
    font-weight: 900;
    font-size: 84px;
    line-height: 1;
    color: var(--paper);
  }
  .divider {
    position: absolute;
    left: 462px; top: 147px;
    width: 6px; height: 215px;
    background: var(--brand-green);
  }
  .person {
    position: absolute;
    left: 489px; top: 140px;
    color: var(--paper);
  }
  .person-name {
    font-size: 27px;
    font-weight: 700;
    line-height: 1.1;
  }
  .person-name .first-name { color: var(--brand-green); }
  .person-title {
    font-size: 20px;
    font-weight: 700;
    margin-top: 2px;
  }
  .contact-list {
    position: absolute;
    left: 489px; top: 230px;
    list-style: none;
    color: var(--paper);
    font-size: 17px;
    font-weight: 700;
    line-height: 22px;
  }
  .contact-list li { display: flex; align-items: flex-start; }
  .contact-icon {
    width: 22px; height: 22px;
    flex: none;
    fill: var(--paper);
  }
</style>
</head>
<body>
<div class="canvas">

  <section class="card-front">
    <div class="front-wordmark">qorvil</div>
    <div class="front-website">www.qorvil.example</div>
  </section>

  <section class="card-back">
    <div class="back-wordmark">qorvil</div>

    <div class="divider"></div>

    <div class="person">
      <h1 class="person-name"><span class="first-name">Olena</span> Dovbush</h1>
      <p class="person-title">Director of Marketing</p>
    </div>

    <ul class="contact-list">
      <li>
        <svg class="contact-icon" viewBox="0 0 22 22" aria-hidden="true"><path d="M4 8h12v7H4z M4 8l6 4 6-4" fill="none" stroke="#fff" stroke-width="1.5"/></svg>
        helen.dovbush@mailvane.example
      </li>
      <li>
        <svg class="contact-icon" viewBox="0 0 22 22" aria-hidden="true"><rect x="6" y="5" width="7" height="12" rx="1" fill="none" stroke="#fff" stroke-width="1.4"/></svg>
        780.555.0187
      </li>
      <li>
        <svg class="contact-icon" viewBox="0 0 22 22" aria-hidden="true"><path d="M4 9q6-4 12 0v2h-3V9H7v2H4z"/><rect x="5" y="12" width="10" height="4" rx="1"/></svg>
        780.555.0187
      </li>
      <li>
        <svg class="contact-icon" viewBox="0 0 22 22" aria-hidden="true"><path d="M10 4a4 4 0 0 1 4 4c0 3-4 8-4 8s-4-5-4-8a4 4 0 0 1 4-4z"/><circle cx="10" cy="8" r="1.5" fill="#898989"/></svg>
        <span>20917 - 87 Ave. Edmonton<br>AB, Canada. T6K 2R8</span>
      </li>
      <li>
        <svg class="contact-icon" viewBox="0 0 22 22" aria-hidden="true"><circle cx="10" cy="12" r="4"/></svg>
        www.qorvil.example
      </li>
    </ul>
  </section>

</div>
</body>
</html>
```